Need Business Card for our Real Estate Business with Sales Executive's Picture

PANTONE 484 C ( RED)

PANTONE 2766 C ( BLUE

Industry/Entity Type

Real Estate

Contact Information for Business Card

Name, Mobile, email, & picture of Person
Agency Phone, address, Web address

Requirements
Must have
• Our Logo Colours, Agent Picture,

```html
<!DOCTYPE html>
<html lang="en">
<head>
<meta charset="utf-8">
<title>Kestrel Business Card</title>
<link href="https://fonts.googleapis.com/css2?family=Cinzel:wght@400;500&family=Roboto:wght@400&display=swap" rel="stylesheet">
<style>
  :root {
    --navy: #0b1436;
    --maroon: #7a1a1e;
    --paper: #f3f3f3;
    --ink-grey: #4e4e4e;
    --backdrop: #e6e2dc;
    --white: #ffffff;
  }
  html, body {
    margin: 0;
    width: 1200px;
    height: 960px;
    overflow: hidden;
    background: var(--backdrop);
  }
  .canvas { position: relative; width: 1200px; height: 960px; }
  .card {
    position: absolute;
    width: 600px;
    height: 342px;
    overflow: hidden;
    box-shadow: 0 2px 6px rgba(0,0,0,0.25);
  }
  .card-front { left: 314px; top: 113px; background: var(--paper); }
  .card-back { left: 311px; top: 472px; background: var(--navy); }

  .brand-name {
    position: absolute;
    font-family: "Cinzel", serif;
    font-weight: 500;
    margin: 0;
    letter-spacing: 1px;
  }
  .card-front .brand-name { left: 26px; top: 34px; font-size: 48px; color: var(--navy); }

  .agent-name {
    position: absolute; left: 26px; top: 134px; margin: 0;
    font-family: "Cinzel", serif; font-weight: 500; font-size: 23px; color: var(--navy);
  }
  .agent-title {
    position: absolute; left: 26px; top: 162px; margin: 0;
    font-family: "Cinzel", serif; font-weight: 500; font-size: 16px; color: var(--maroon);
  }
  .contact {
    position: absolute; left: 26px; top: 195px;
    font-family: "Roboto", sans-serif; font-size: 14.5px; color: var(--ink-grey); line-height: 19px;
  }
  .address { margin: 0 0 6px; }
  .contact-list { list-style: none; margin: 0; padding: 0; }
  .contact-list li { display: flex; align-items: center; gap: 9px; }
  .contact-list svg { width: 13px; height: 13px; fill: var(--navy); }

  .web-band {
    position: absolute; left: 0; bottom: 0; width: 100%; height: 34px; background: var(--navy);
  }
  .web-band span {
    position: absolute; left: 27px; top: 8px;
    font-family: "Cinzel", serif; font-size: 15px; letter-spacing: 5px; color: var(--white);
  }
  .agent-photo {
    position: absolute; left: 336px; top: 8px; width: 260px; height: 334px;
    background: linear-gradient(180deg, #e9e6e3 0%, #c9a58c 30%, #2a4a9a 55%, #1d3270 100%);
  }

  .card-back .brand-name {
    left: 0; width: 100%; top: 186px; text-align: center; font-size: 46px; color: var(--white);
  }
  .back-web {
    position: absolute; left: 0; width: 100%; top: 296px; text-align: center;
    font-family: "Roboto", sans-serif; font-size: 14px; letter-spacing: 4px; color: var(--white);
  }
</style>
</head>
<body>
<main class="canvas">
  <section class="card card-front">
    <h1 class="brand-name">KESTREL</h1>
    <h2 class="agent-name">DANIEL REYES</h2>
    <p class="agent-title">CEO/FOUNDER</p>
    <div class="contact">
      <p class="address">2140 Alder Court<br>Juneau, Alaska 36812</p>
      <ul class="contact-list">
        <li><svg viewBox="0 0 24 24"><path d="M6.6 10.8a15 15 0 0 0 6.6 6.6l2.2-2.2c.3-.3.7-.4 1-.2 1.1.4 2.3.6 3.6.6.6 0 1 .4 1 1V20c0 .6-.4 1-1 1A17 17 0 0 1 3 4c0-.6.4-1 1-1h3.5c.6 0 1 .4 1 1 0 1.3.2 2.5.6 3.6.1.3 0 .7-.2 1z"/></svg>512 304 7781</li>
        <li><svg viewBox="0 0 24 24"><path d="M7 1h10a2 2 0 0 1 2 2v18a2 2 0 0 1-2 2H7a2 2 0 0 1-2-2V3a2 2 0 0 1 2-2zm0 3v14h10V4z"/></svg>719 562 0843</li>
        <li><svg viewBox="0 0 24 24"><path d="M2 5h20v14H2zm2 2v.5l8 5 8-5V7z"/></svg>dan@kestrel.com</li>
      </ul>
    </div>
    <div class="web-band"><span>WWW.KESTREL.COM</span></div>
    <div class="agent-photo" role="img" aria-label="Portrait photo of the agent in a navy suit and striped tie"></div>
  </section>

  <section class="card card-back">
    <h1 class="brand-name">KESTREL</h1>
    <p class="back-web">www.kestrel.com</p>
  </section>
</main>
</body>
</html>
```